Independent Artist - Album Cover Design

I need a full album cover design for my debut album Velvet Tide Rising. The album is a love-inspired, passionate, soulful, relationship laden album. An album that can relate to anyone in love (or lust/obsession), going through ups and downs of relationships,and overcoming any hardships and enjoying the joys of true love, sex, and companionship. My first thoughts are a black and white design with the color red poppin off in there maybe in some of the lettering but I am open to some creative ideas. Looking for something clean and sexy that represents what the album is about. I was thinking maybe having a photo of myself on there but don't really have any that would work This Hour but I can take some and send a link if you have some good ideas.
Updates

My Artist name if I didnt mention before is Dravelle. I would like that on the album cover as well. Also I need a full album cover Front and Back. Below is the track list if you could incorporate that as well. And below is also a link to some photos. Thank you.

https://www.fileharbor.example/sh/qk4wumbrtz8plvd/KetPorvaxN

1 .Midnight Skin (Feat. Teddy Quarrelstone)
2.  Velour Heat (Feat. Dime Rek)
3 .Feel the Ember (Feat. Nalo)
4 . Lift Me Over
5. Slipshada
6.  Near Me (Feat. Dime Rek)
7 .She Wears Me Well Now
8 . This Hour
9 . All Night Again
10.  Down The Hall
11.  We Shall
12 . Seasons Of Passion

New Clearer Pictures Posted to fileharbor folder. Thanks.

https://www.fileharbor.example/sh/qk4wumbrtz8plvd/MMRt7h31FvZwQsKyNoragxunt

```html
<!DOCTYPE html>
<html lang="en">
<head>
<meta charset="utf-8">
<title>Dravelle – Velvet Tide Rising album cover</title>
<link rel="stylesheet" href="https://fonts.googleapis.com/css2?family=Archivo+Black&family=Italianno&family=Parisienne&display=swap">
<style>
  :root{
    --page:#ffffff;
    --sleeve-dark:#0d0d0d;
    --sleeve-mid:#262626;
    --spine:#141414;
    --crimson:#8e0c16;
    --crimson-deep:#6f0910;
    --label-ink:#1a1a1a;
    --script-red:#9a1118;
    --peach:#f2ad8f;
    --photo-a:#3a3330;
    --photo-b:#1b1716;
  }
  html,body{margin:0;padding:0;}
  body{width:1200px;height:1000px;overflow:hidden;background:var(--page);position:relative;}
  .sleeve{position:absolute;left:2px;top:221px;width:1196px;height:571px;overflow:hidden;
    background:radial-gradient(ellipse at 50% 35%,var(--sleeve-mid) 0%,var(--sleeve-dark) 75%);}
  .panel{position:absolute;top:0;height:100%;overflow:hidden;}
  .panel--back{left:0;width:571px;}
  .panel--spine{left:571px;width:55px;background:linear-gradient(90deg,#0a0a0a,var(--spine) 40%,#0b0b0b);
    box-shadow:inset 1px 0 0 #2b2b2b, inset -1px 0 0 #2b2b2b;}
  .panel--front{left:626px;width:570px;}
  .band{position:absolute;height:63px;background:linear-gradient(180deg,var(--crimson),var(--crimson-deep));
    border-radius:14px 0 0 14px;box-shadow:0 2px 6px rgba(0,0,0,.6);}
  .panel--back .band{left:213px;top:259px;width:360px;}
  .panel--front .band{left:75px;top:262px;width:500px;}
  .artist-photo{position:absolute;background:linear-gradient(160deg,var(--photo-a),var(--photo-b));
    border-radius:120px 120px 0 0;}
  .panel--back .artist-photo{left:300px;top:178px;width:255px;height:393px;}
  .panel--front .artist-photo{left:160px;top:152px;width:265px;height:419px;}
  .name-tag{position:absolute;background:var(--crimson);display:flex;align-items:center;justify-content:center;
    font-family:"Archivo Black",sans-serif;color:var(--label-ink);transform:rotate(-16deg);letter-spacing:1px;}
  .panel--back .name-tag{left:232px;top:448px;width:334px;height:74px;font-size:50px;}
  .panel--front .name-tag{left:50px;top:80px;width:380px;height:88px;font-size:60px;}
  .album-title{position:absolute;font-family:"Parisienne",cursive;margin:0;font-weight:400;white-space:nowrap;}
  .panel--back .album-title{left:60px;top:22px;font-size:34px;color:var(--script-red);}
  .panel--front .album-title{left:112px;top:470px;font-size:50px;color:var(--peach);}
  .tracklist{position:absolute;left:50px;top:78px;margin:0;padding:0;list-style:none;
    font-family:"Italianno",cursive;font-size:21px;line-height:24.4px;color:var(--script-red);}
  .spine-title{position:absolute;left:14px;top:150px;font-family:"Parisienne",cursive;font-size:21px;
    color:var(--script-red);writing-mode:vertical-rl;white-space:nowrap;}
  .spine-tag{position:absolute;left:10px;top:346px;width:42px;height:184px;background:var(--crimson);
    display:flex;align-items:center;justify-content:center;}
  .spine-tag span{writing-mode:vertical-rl;font-family:"Archivo Black",sans-serif;font-size:27px;color:var(--label-ink);}
</style>
</head>
<body>
  <div class="sleeve">
    <section class="panel panel--back">
      <div class="band"></div>
      <div class="artist-photo" role="img" aria-label="Photo of the artist in profile, tipping a dark hat, tattooed arm, black tank top"></div>
      <h2 class="album-title">Velvet Tide Rising</h2>
      <ol class="tracklist">
        <li>1. Midnight Skin (Feat. Teddy Quarrelstone)</li>
        <li>2. Velour Heat (Feat. Dime Rek)</li>
        <li>3. Feel the Ember (Feat. Nalo)</li>
        <li>4. Lift Me Over</li>
        <li>5. Slipshada</li>
        <li>6. Near Me (Feat. Dime Rek)</li>
        <li>7. She Wears Me Well Now</li>
        <li>8. This Hour</li>
        <li>9. All Night Again</li>
        <li>10. Down The Hall</li>
        <li>11. We Shall</li>
        <li>12. Seasons Of Passion</li>
      </ol>
      <div class="name-tag">DRAVELLE</div>
    </section>
    <section class="panel panel--spine">
      <div class="spine-title">Velvet Tide Rising</div>
      <div class="spine-tag"><span>DRAVELLE</span></div>
    </section>
    <section class="panel panel--front">
      <div class="band"></div>
      <div class="artist-photo" role="img" aria-label="Photo of the artist in profile, tipping a dark hat, tattooed arm, black tank top"></div>
      <div class="name-tag">DRAVELLE</div>
      <h1 class="album-title">Velvet Tide Rising</h1>
    </section>
  </div>
</body>
</html>
```